Quick Straightforward Billboard Redesign

- Design billboard sized for 10 foot' x 36' foot width live area size and please include bleeds 6" around all sides
- Exact blue color match is imperative in headline, logo, phone number bubble or wherever used. C-83 / M-45 / Y-1 / K-0-
- What I hope to illustrate is that our company offers the best porch screening in the area area, in regards to quality, expertise, durability, storms proof, but we do not build screen porches.
- Current board is attached below from previous designer, and as you can see sizing was off, white space on edges make it appear to be sized incorrectly.
- I also attached my own little mock up idea well well if it helps, favorite image, logo, headline, etc and ideas perhaps on expanding or making this better?

Thanks so much!

Target Market(s)

Drivers and passengers, Southeastern NC, are of immense new construction and high end homes.

Industry/Entity Type

Construction

Colors
0054AA
0677BA
7BADD7
CADEEF
E8F1F8

Requirements
Must have
• Blue color matching
Nice to have
• Design spins or other thoughts on my little mock up

```html
<!DOCTYPE html>
<html lang="en">
<head>
<meta charset="utf-8">
<title>Billboard – Tidewater Mesh Co.</title>
<link href="https://fonts.googleapis.com/css2?family=Roboto+Condensed:wght@800;900&family=Oswald:wght@500&display=swap" rel="stylesheet">
<style>
  :root {
    --brand-blue: #2d8bee;
    --brand-blue-deep: #1f6fe0;
    --coast-green: #3ee83a;
    --paper: #ffffff;
    --photo-light: #e9eef1;
    --photo-sky: #a9cdea;
    --photo-lawn: #b4cf98;
    --panel-edge: rgba(0, 0, 0, 0.12);
    --panel-shadow: rgba(0, 0, 0, 0.38);
  }
  html, body {
    margin: 0;
    width: 1200px;
    height: 1000px;
    overflow: hidden;
    background: var(--paper);
  }
  .billboard {
    position: absolute;
    left: 74px;
    top: 354px;
    width: 1052px;
    height: 292px;
    background: var(--paper);
    overflow: hidden;
    box-shadow: 1px 3px 5px var(--panel-shadow), 0 0 0 1px var(--panel-edge);
  }
  .porch-photo {
    position: absolute;
    left: 548px;
    top: 0;
    width: 504px;
    height: 292px;
    background: linear-gradient(180deg,
      var(--photo-light) 0%,
      var(--photo-sky) 50%,
      var(--photo-lawn) 100%);
    -webkit-mask-image: linear-gradient(90deg, transparent 0%, #000 30%);
            mask-image: linear-gradient(90deg, transparent 0%, #000 30%);
  }
  .headline {
    position: absolute;
    left: 30px;
    margin: 0;
    font-family: "Roboto Condensed", "Arial Narrow", sans-serif;
    font-weight: 900;
    line-height: 1;
    white-space: nowrap;
  }
  .headline--main {
    top: 26px;
    font-size: 69px;
    color: var(--brand-blue);
    letter-spacing: 0.4px;
  }
  .headline--sub {
    top: 106px;
    font-size: 61px;
    color: var(--coast-green);
    letter-spacing: 0.4px;
  }
  .brand {
    position: absolute;
    left: 31px;
    top: 215px;
    display: flex;
    align-items: flex-end;
    gap: 14px;
  }
  .brand__mark {
    width: 44px;
    height: 44px;
    background: var(--brand-blue-deep);
  }
  .brand__name {
    font-family: "Oswald", "Arial Narrow", sans-serif;
    font-weight: 500;
    font-size: 38px;
    line-height: 0.82;
    color: var(--brand-blue-deep);
    text-transform: uppercase;
    letter-spacing: -0.5px;
  }
  .phone-tag {
    position: absolute;
    left: 673px;
    top: 31px;
    width: 349px;
    height: 57px;
    background: var(--brand-blue);
    display: flex;
    align-items: center;
    justify-content: center;
    font-family: "Roboto Condensed", "Arial Narrow", sans-serif;
    font-weight: 900;
    font-size: 45px;
    color: var(--paper);
    letter-spacing: 1.5px;
  }
</style>
</head>
<body>
  <section class="billboard">
    <div class="porch-photo" role="img" aria-label="Photo of a screened covered porch with outdoor furniture overlooking a lawn and lake"></div>

    <h1 class="headline headline--main">Screen Your Porch.</h1>
    <p class="headline headline--sub">Built for the Coast.</p>

    <div class="brand">
      <span class="brand__mark" aria-hidden="true"></span>
      <span class="brand__name">Tidewater Mesh Co.</span>
    </div>

    <div class="phone-tag">910.555.0142</div>
  </section>
</body>
</html>
```